Establishing a website for a non profit organisation

The foundation is called:

German: Edle Alte Bruderschaft des Hofes Lindenmark e.V.

Englisch (Translation): Noble old Brotherhood of Court Lindenmark e.V.

The foundation is a legal nonprofit organization with the purpose to help people in need. The foundation - a charitable organization - donates funds and supports solely and directly people living in Frankfurt and in Germany.

In some cases the foundation works together with other charitable organizations that support projects to help people in need.

The foundation also functions as trustee with powers of administration of property in trust with a legal obligation to administer it solely for the purposes specified. The purpose is not to generate/obtain wealth for shareholders but to respectfully execute the benevolent intentions of the founders/testators in the interest of the legatee.

The foundation was established in 1408.

The website should give a good and easy overview about the foundation work.
It should be easy to figure out how to participate and help the organisation.
Either you can participate with a one time donation, with a regular donation or with a testament.

For those with donation it is possible to hand over an contribution receipt for tax purposes.

The main color should be red: RGB R:229 - G:47 - B:34

```html
<!DOCTYPE html>
<html lang="en">
<head>
<meta charset="utf-8">
<title>Noble old Brotherhood of Court Lindenmark e.V.</title>
<link rel="stylesheet" href="https://fonts.googleapis.com/css2?family=Fjalla+One&family=Open+Sans:wght@400;600&family=Oxygen:wght@300;400;700&display=swap">
<style>
:root{
  --red:#e52f22;
  --dark:#464a4d;
  --panel:#e9e5e5;
  --panel-side:#dedad9;
  --text:#3a3a3a;
  --white:#ffffff;
}
*{box-sizing:border-box;margin:0;padding:0}
html,body{width:1044px;height:1200px;overflow:hidden;background:var(--white)}
body{font-family:"Oxygen",sans-serif;color:var(--text)}
.page{position:relative;width:1000px;height:1149px;transform:scale(1.044);transform-origin:0 0}
.abs{position:absolute}

.topbar{right:42px;top:9px;font-family:"Open Sans",sans-serif;font-size:14px;color:#666}
.topbar b{font-weight:600;color:#333;margin-right:10px}
.topbar .sep{margin:0 6px}
.site-title{left:31px;top:27px;font-family:"Fjalla One",sans-serif;font-size:25px;color:var(--red);letter-spacing:.2px}

.mainnav{left:0;top:73px;width:1000px;height:48px;background:var(--dark);border-bottom:3px solid var(--red);display:flex;align-items:center;padding-left:25px}
.mainnav a{font-family:"Open Sans",sans-serif;font-weight:600;font-size:14px;color:var(--white);text-decoration:none;text-transform:uppercase;height:45px;line-height:48px;padding:0 9px;margin-right:1px}
.mainnav a.active{background:var(--red);padding:0 13px}
.mainnav a:last-child{margin-left:8px}

.hero{left:20px;top:131px;width:961px;height:472px;background:linear-gradient(180deg,#b7cc8a 0%,#c9d6a4 30%,#9bb56a 70%,#c6c9a5 100%)}
.mission{left:35px;top:555px;width:932px;height:83px;background:var(--red);color:var(--white);font-weight:300;font-size:23.5px;line-height:29px;padding:9px 48px 0 27px;text-align:justify;border-radius:3px 3px 0 0}

.features{left:35px;top:638px;width:932px;height:277px;background:linear-gradient(180deg,var(--panel) 78%,#d9d5d5 100%);border-radius:0 0 4px 4px}
.feature{top:0;height:277px;text-align:center}
.feature.donate{left:647px;width:257px;background:linear-gradient(180deg,var(--panel-side) 80%,#d5d1d1 100%)}
.icon{position:absolute;width:66px;height:66px;border-radius:50%;background:var(--dark)}
.icon svg{width:66px;height:66px}
.feature h2{position:absolute;font-weight:300;font-size:24px;color:var(--red);white-space:nowrap}
.feature p{position:absolute;font-size:12.5px;line-height:16px;text-align:justify;color:#444}
.btn-more{position:absolute;width:101px;height:36px;border:2px solid #555;border-radius:4px;background:#eceaea;font-family:"Oxygen",sans-serif;font-size:13px;color:#333;line-height:32px}
.choice{position:absolute;left:40px;font-size:13px;color:#444;display:flex;align-items:center}
.choice i{display:inline-block;width:12px;height:12px;border:1px solid #999;border-radius:50%;background:#fafafa;margin-right:7px}
.amount{position:absolute;left:37px;top:205px;width:67px;height:32px;background:var(--white);border:1px solid #bbb;border-radius:3px}
.btn-donate{position:absolute;left:125px;top:202px;width:101px;height:35px;background:var(--red);color:var(--white);font-size:16px;line-height:35px;border-radius:2px}

.footer{left:0;top:940px;width:1000px;height:209px;background:var(--dark);border-top:3px solid var(--red);color:var(--white)}
.footer-name{left:38px;top:25px;font-family:"Fjalla One",sans-serif;font-size:18.5px;line-height:25px}
.footer-address{left:38px;top:77px;font-size:13px}
.footer-contact{left:38px;font-size:10px}
.footer-contact b{font-weight:700}
.footer h3{font-family:"Open Sans",sans-serif;font-weight:600;font-size:14px;position:absolute;top:22px}
.links{left:328px;top:0}
.links ul{list-style:none;position:absolute;top:50px;width:200px}
.links li{font-family:"Open Sans",sans-serif;font-size:13px;line-height:24px;color:#eee}
.social{left:593px;top:0}
.social-item{position:absolute;left:0;display:flex;align-items:center;font-family:"Open Sans",sans-serif;font-size:15px;width:200px}
.social-item i{display:inline-block;width:20px;height:20px;border-radius:50%;background:#e8e8e8;margin:0 23px 0 1px}
</style>
</head>
<body>
<div class="page">
  <div class="abs topbar"><b>Call</b>069 275104486<span class="sep">|</span><b>Email</b>hello@lindenmark-help.org</div>
  <h1 class="abs site-title">Noble old Brotherhood of Court Lindenmark e.V.</h1>

  <nav class="abs mainnav">
    <a class="active">Home</a><a>History of the foundation</a><a>What we do today</a><a>Posibilities to donate</a><a>Receive donations</a><a>News</a><a>Contact</a>
  </nav>

  <div class="abs hero" role="img" aria-label="Photo of three smiling children outdoors holding a cardboard sign reading Give"></div>
  <p class="abs mission">We are a charitable organization that donates funds and supports solely and directly people living in Frankfurt and in Germany.</p>

  <section class="abs features">
    <div class="abs feature" style="left:0;width:300px">
      <div class="icon" style="left:116px;top:30px">
        <svg viewBox="0 0 66 66"><g fill="#fff">
          <circle cx="21" cy="26" r="3"/><rect x="18" y="30" width="6" height="10" rx="1.5"/><rect x="18.5" y="38" width="2" height="8"/><rect x="21.5" y="38" width="2" height="8"/>
          <circle cx="33" cy="26" r="3"/><rect x="30" y="30" width="6" height="10" rx="1.5"/><rect x="30.5" y="38" width="2" height="8"/><rect x="33.5" y="38" width="2" height="8"/>
          <circle cx="45" cy="26" r="3"/><rect x="42" y="30" width="6" height="10" rx="1.5"/><rect x="42.5" y="38" width="2" height="8"/><rect x="45.5" y="38" width="2" height="8"/>
          <rect x="14" y="31" width="38" height="2"/></g></svg>
      </div>
      <h2 style="left:88px;top:103px">Who we are</h2>
      <p style="left:35px;top:142px;width:250px">Lorem ipsum dolor sit amet, et omnium vulputate honestatis vix. No nonumy appellantur ius.</p>
      <div class="btn-more" style="left:89px;top:213px">Read more</div>
    </div>

    <div class="abs feature" style="left:300px;width:330px">
      <div class="icon" style="left:107px;top:25px">
        <svg viewBox="0 0 66 66"><path fill="#fff" d="M33 50 L17 34 C11 28 15 18 23 18 C27 18 30 20 33 24 C36 20 39 18 43 18 C51 18 55 28 49 34 Z"/><path d="M22 36 L30 28 M27 41 L35 33 M32 45 L40 37" stroke="#464a4d" stroke-width="2.5" fill="none"/></svg>
      </div>
      <h2 style="left:69px;top:103px">Where to get help</h2>
      <p style="left:37px;top:140px;width:265px">Lorem ipsum dolor sit amet, et omnium vulputate honestatis vix. No nonumy appellantur ius.</p>
      <div class="btn-more" style="left:114px;top:217px">Read more</div>
    </div>

    <div class="abs feature donate">
      <div class="icon" style="left:85px;top:24px">
        <svg viewBox="0 0 66 66"><path fill="#fff" d="M33 48 L19 34 C13 28 17 19 24 19 C28 19 31 21 33 25 C35 21 38 19 42 19 C49 19 53 28 47 34 Z"/></svg>
      </div>
      <h2 style="left:48px;top:104px">Want to help</h2>
      <div class="choice" style="top:150px"><i></i>One time donation</div>
      <div class="choice" style="top:174px"><i></i>Recurring monthly donation</div>
      <div class="amount"></div>
      <div class="btn-donate">DONATE</div>
    </div>
  </section>

  <footer class="abs footer">
    <div class="abs footer-name">Noble old Brotherhood<br>of Court Lindenmark e.V.</div>
    <div class="abs footer-address">14 Lindenweg Frankfurt, Germany</div>
    <div class="abs footer-contact" style="top:99px"><b>Phone:</b> 069 275104486</div>
    <div class="abs footer-contact" style="top:123px"><b>Mail:</b> hello@lindenmark-help.org</div>

    <div class="abs links">
      <h3>LINKS</h3>
      <ul>
        <li>History of the foundation</li><li>What we do today</li><li>Posibilities to donate</li><li>Receive donations</li><li>News</li><li>Contact</li>
      </ul>
    </div>

    <div class="abs social">
      <h3>SOCIAL</h3>
      <div class="social-item" style="top:53px"><i></i>Circlebook</div>
      <div class="social-item" style="top:108px"><i></i>Chirpline</div>
    </div>
  </footer>
</div>
</body>
</html>
```